Online-Marketing Material für Autorin, Ghostwriterin, Buchmentorin
Thank you so much, Glimmerfox, for the great work you did for me. I recommend working with you to everybody who wishes to have very well crafted, efficient marketing materials that exactly meet your CI in style and emotion. All very best :)
Zielgruppe
Ich bin Autorin, Ghostwriterin, Buchmentorin und helfe Unternehmern und Selbständigen auf dem Weg zum eigenen Buch. Meine Zielgruppe sind Menschen, die ein eigenes Unternehmen haben und durch ein Expertenbuch ihren Expertenstatus steigern wollen. Hauptzielgruppe sind z. B. Speaker, Trainer, Coaches, Berater.
Aufgabenstellung
Dieses Design dient dem Online-Marketing für meine neue Online-Akademie (Online Kurse und Masterclasses).
Die Kurse dienen den Kunden dazu, von der ersten Idee bis zum fertigen Buch alles Wissenswerte und Essenzielle über das professionelle, leichte und erfolgreiche Bücherschreiben, Publizieren und die Buchvermarktung zu erfahren.
Ich möchte, dass das Design eine gewisse 'Größe' ausstrahlt, sodass sich Unternehmer:innen angezogen fühlen, die bereit sind, in sich und die Zusammenarbeit mit mir zu investieren. Gleichzeitig soll das Design Leichtigkeit und Machbarkeit des Buchschreibprozesses und der Umsetzung mit mir ausstrahlen. Meine Firmenfarben sind Türkis und Sonnengelb.
Ich bin unentschlossen, ob ein Foto von mir mit aufgegriffen werden sollte. Ich lade mal eins mit hoch :)

```html
<!DOCTYPE html>
<html lang="de">
<head>
<meta charset="utf-8">
<title>Von der ersten Idee bis zum fertigen Buch</title>
<link rel="stylesheet" href="https://fonts.googleapis.com/css2?family=Arimo:wght@700&display=swap">
<style>
  :root {
    --stage: #f2f2f2;
    --sun: #fcd945;
    --sun-deep: #f6c92e;
    --sky: #7fdcf8;
    --sky-deep: #5fd3ff;
    --ink: #141a2e;
    --teal: #2aa7d3;
    --paper: #ffffff;
    --button: #f7d84a;
    --photo-top: #3fb4e4;
    --photo-bottom: #2a9fd4;
  }
  * { box-sizing: border-box; margin: 0; padding: 0; }
  html, body { width: 1200px; height: 1200px; overflow: hidden; }
  body {
    background: var(--stage);
    font-family: "Arimo", Arial, sans-serif;
    font-weight: 700;
    color: var(--ink);
    position: relative;
  }
  .ad {
    position: absolute;
    left: 272px; top: 238px;
    width: 705px; height: 705px;
    overflow: hidden;
    background: var(--sun);
  }
  .desk-scene {
    position: absolute; left: 0; top: 0;
    width: 705px; height: 489px;
    background: linear-gradient(120deg, var(--sun) 0%, var(--sun-deep) 65%, #f4f2ea 100%);
  }
  .note-panel {
    position: absolute;
    left: -119px; top: 48px;
    width: 380px; height: 450px;
    background: var(--paper);
    border-radius: 10px;
    transform: rotate(-14deg);
    transform-origin: 100% 0;
    box-shadow: 0 4px 12px rgba(0,0,0,0.12);
  }
  .info-band {
    position: absolute; left: 0; top: 489px;
    width: 705px; height: 216px;
    background: linear-gradient(180deg, var(--sky) 0%, var(--sky-deep) 100%);
  }
  .headline {
    position: absolute; left: 0; top: 0;
    width: 705px; height: 489px;
    font-size: inherit;
  }
  .headline span {
    position: absolute;
    white-space: nowrap;
    line-height: 1;
    transform: rotate(-14deg);
    transform-origin: 0 0.847em;
  }
  .line-small { font-size: 42px; }
  .line-large { font-size: 64px; }
  .line-von { left: 55px; top: 133px; }
  .line-ersten { left: 63px; top: 183px; }
  .line-idee { left: 100px; top: 239px; }
  .line-bis { left: 108px; top: 307px; }
  .line-fertigen { left: 83px; top: 359px; }
  .line-buch {
    left: 149px; top: 409px;
    color: var(--teal);
    text-shadow: -4px 4px 0 var(--sun);
  }
  .benefits {
    position: absolute; left: 32px; top: 516px;
    list-style: none;
  }
  .benefits li {
    position: relative;
    padding-left: 26px;
    font-size: 14px;
    line-height: 19px;
    margin-bottom: 17px;
  }
  .benefits svg {
    position: absolute; left: 0; top: 2px;
  }
  .cta {
    position: absolute; left: 86px; top: 633px;
    width: 160px; height: 38px;
    background: var(--button);
    border-radius: 6px;
    box-shadow: 0 4px 8px rgba(0,0,0,0.2);
    display: flex; align-items: center; justify-content: center;
    font-size: 17px;
    color: var(--ink);
    text-decoration: none;
  }
  .portrait {
    position: absolute;
    left: 330px; top: 160px;
    width: 390px; height: 560px;
    background: linear-gradient(180deg, var(--photo-top) 0%, var(--photo-bottom) 100%);
    border: 5px solid var(--paper);
    border-radius: 24px 24px 0 0;
  }
</style>
</head>
<body>
  <div class="ad">
    <div class="desk-scene" role="img" aria-label="Schreibtisch von oben mit Notizblock, Bleistift und Laptop auf gelbem Grund"></div>
    <div class="note-panel"></div>
    <div class="info-band"></div>

    <h1 class="headline">
      <span class="line-small line-von">Von der</span>
      <span class="line-large line-ersten">Esten</span>
      <span class="line-large line-idee">Idee</span>
      <span class="line-small line-bis">bis zum</span>
      <span class="line-large line-fertigen">Fertigen</span>
      <span class="line-large line-buch">Buch</span>
    </h1>

    <ul class="benefits">
      <li>
        <svg width="18" height="14" viewBox="0 0 18 14"><path d="M1 7 L6 12 L17 1" fill="none" stroke="#141a2e" stroke-width="2.2"/></svg>
        Professionelle, leichte und<br>erfolgreiche Bücherschreiben
      </li>
      <li>
        <svg width="18" height="14" viewBox="0 0 18 14"><path d="M1 7 L6 12 L17 1" fill="none" stroke="#141a2e" stroke-width="2.2"/></svg>
        Publizieren und<br>die Buchvermarktung zu erfahren
      </li>
    </ul>

    <a class="cta" href="#">JETZT BUCHEN</a>

    <div class="portrait" role="img" aria-label="Porträtfoto der Autorin in türkisem Oberteil, freigestellt mit weißem Rand"></div>
  </div>
</body>
</html>
```